you will use Ai to Copy the website Quellabyx.com to come up with the basic frame work and it will give you the understanding of how I would like Zandoprik.com to be like. Zandoprik.com is a peer to peer rv rental site very similar to both of the other rv rental sites the difference is that are commission based 20% and above per rental and we will be one flat monthly rate and they keep all the earnings. Below is photo that will help you with the color scheme and the look and feel of the design

```html
<!DOCTYPE html>
<html lang="en">
<head>
<meta charset="utf-8">
<title>Zandoprik — Peer-to-peer RV rentals</title>
<link href="https://fonts.googleapis.com/css2?family=Archivo+Black&family=Lato:ital,wght@0,400;0,700;0,900;1,400&display=swap" rel="stylesheet">
<style>
:root{
  --navy:#0e1829;
  --navy-2:#121f35;
  --card:#16243d;
  --card-line:#26385a;
  --gold:#e49a2f;
  --gold-2:#f1b34a;
  --gold-deep:#c57a1c;
  --ink:#0f1b30;
  --muted:#8fa0bd;
  --light:#f3f5f9;
  --white:#ffffff;
  --red:#d9463b;
}
*{box-sizing:border-box;margin:0;padding:0}
html,body{width:1200px;height:1200px;overflow:hidden;background:#fff}
body{position:relative;font-family:"Lato",sans-serif;color:var(--white)}
.head{font-family:"Archivo Black",sans-serif;font-weight:400;letter-spacing:-.2px}
.page{position:absolute;width:638px;transform:scale(.625);transform-origin:0 0;overflow:hidden;box-shadow:0 20px 50px rgba(15,25,45,.25)}
.page-home{left:189px;top:88px;height:1407px;background:var(--navy)}
.page-owners{left:619px;top:139px;height:1568px;background:var(--navy)}
.abs{position:absolute}

.rule{position:absolute;left:50%;width:24px;height:2px;margin-left:-12px;background:var(--gold);border-radius:2px}
.eyebrow{position:absolute;left:50%;transform:translateX(-50%);border:1px solid var(--gold);color:var(--gold);font-size:5px;font-weight:900;letter-spacing:1px;padding:3px 7px;border-radius:20px;white-space:nowrap;text-transform:uppercase}
.sec-title{position:absolute;left:0;right:0;text-align:center;font-size:19px;line-height:24px}
.sec-lede{position:absolute;left:50%;transform:translateX(-50%);text-align:center;font-size:7.4px;line-height:12px;color:#b8c4da}
.btn-gold{background:var(--gold);color:var(--ink);font-weight:900;border-radius:20px;display:flex;align-items:center;justify-content:center;box-shadow:0 2px 6px rgba(228,154,47,.35)}

.nav{position:absolute;left:0;top:0;width:638px;height:35px;background:var(--navy);display:flex;align-items:center;z-index:2}
.brand{position:absolute;font-weight:900;font-size:11px;color:var(--white);letter-spacing:-.2px}
.nav .brand{left:52px;top:10px}
.nav-links{position:absolute;left:229px;top:13px;display:flex;gap:14px;font-size:6.2px;font-weight:700}
.nav-signin{position:absolute;left:503px;top:13px;font-size:6.2px;font-weight:700}
.nav-cta{position:absolute;left:532px;top:7px;width:57px;height:20px;font-size:6px}

.hero{position:absolute;left:0;top:35px;width:638px;height:600px;
  background:linear-gradient(180deg,rgba(14,24,41,.2) 0%,rgba(14,24,41,0) 25%,rgba(14,24,41,.5) 60%,var(--navy) 100%),
  linear-gradient(90deg,rgba(14,24,41,.85) 0%,rgba(14,24,41,.35) 55%,rgba(14,24,41,.1) 100%),
  linear-gradient(175deg,#1b2a44 0%,#3a4a63 20%,#b0703a 34%,#5a4a44 44%,#24304a 60%,#0e1829 100%)}
.hero-badge{left:40px;top:47px;border:1px solid var(--gold);color:var(--gold);font-size:4.6px;font-weight:900;letter-spacing:.8px;padding:3px 6px;border-radius:20px}
.hero-title{left:39px;top:73px;font-size:30px;line-height:35px;width:380px}
.hero-title span{color:var(--gold)}
.hero-lede{left:39px;top:150px;width:300px;font-size:8px;line-height:14.5px;color:#d5dbe7}
.hero-lede b{color:#fff}
.search{left:39px;top:207px;width:449px;height:80px;background:#fff;border-radius:7px;color:var(--ink);box-shadow:0 10px 30px rgba(0,0,0,.35)}
.search-tabs{position:absolute;left:14px;top:10px;display:flex;gap:16px;font-size:6px;font-weight:700}
.search-tabs .on{border-bottom:1.5px solid var(--gold);padding-bottom:6px}
.search-tabs .off{color:#5a6c8c}
.search-line{position:absolute;left:0;right:0;top:28px;height:1px;background:#e6e9ef}
.field{position:absolute;top:36px}
.field label{display:block;font-size:4.6px;font-weight:900;letter-spacing:.8px;color:#6b7a95;margin-bottom:3px}
.field .box{height:22px;border:1px solid #e1e5ec;border-radius:4px;display:flex;align-items:center;gap:5px;padding-left:8px;font-size:6.2px;font-weight:700}
.search-btn{position:absolute;left:377px;top:50px;width:62px;height:22px;font-size:6.2px;gap:4px}
.popular{left:39px;top:302px;display:flex;align-items:center;gap:5px;font-size:5.6px;color:#c4cde0}
.chip{border:1px solid #3b4d6c;border-radius:20px;padding:4px 7px;color:#fff;font-weight:700;background:rgba(14,24,41,.5)}
.hero-divider{left:39px;top:348px;width:560px;height:1px;background:rgba(255,255,255,.1)}
.stat{top:366px;width:90px}
.stat b{display:block;font-family:"Archivo Black",sans-serif;font-weight:400;color:var(--gold);font-size:11px;margin-bottom:4px}
.stat span{display:block;font-size:5.4px;line-height:8px;color:#b8c4da}
.stat-sep{top:366px;width:1px;height:30px;background:rgba(255,255,255,.12)}

.mode{top:519px;width:263px;height:154px;border-radius:8px;overflow:hidden}
.mode-photo{position:absolute;inset:0}
.mode-copy{position:absolute;left:13px;top:58px;width:190px}
.mode-copy h3{font-size:10.5px;margin-bottom:6px}
.mode-copy p{font-size:5.8px;line-height:9px;color:#dde3ee}
.mode-btn{position:absolute;left:13px;top:120px;height:18px;padding:0 11px;font-size:5.6px}

.filters{left:0;right:0;top:891px;display:flex;justify-content:center;gap:5px}
.filters .chip{background:transparent;font-size:5.6px}
.filters .chip.on{background:var(--gold);border-color:var(--gold);color:var(--ink)}
.rv{width:172px;height:191px;background:var(--card);border:1px solid var(--card-line);border-radius:7px;overflow:hidden}
.rv-photo{position:absolute;left:0;top:0;width:100%;height:107px}
.rv-tag{position:absolute;left:7px;top:7px;background:var(--navy);color:#fff;font-size:4.8px;font-weight:900;padding:3px 5px;border-radius:10px}
.rv-fav{position:absolute;right:7px;top:7px;width:13px;height:13px;border-radius:50%;background:rgba(14,24,41,.7);display:flex;align-items:center;justify-content:center}
.rv-meta{position:absolute;left:8px;top:116px;font-size:4.8px;color:#c2cbdc}
.rv-name{position:absolute;left:8px;top:128px;font-size:7px;font-weight:900}
.rv-loc{position:absolute;left:8px;top:144px;font-size:5px;color:#9fadc6;display:flex;align-items:center;gap:3px}
.rv-line{position:absolute;left:8px;right:8px;top:158px;height:1px;background:var(--card-line)}
.rv-price{position:absolute;left:8px;top:167px;display:flex;align-items:center;gap:3px;font-size:4.6px;color:#9fadc6}
.rv-price b{font-family:"Archivo Black",sans-serif;font-weight:400;color:var(--gold);font-size:8.5px}
.fee{border:1px solid var(--gold);color:var(--gold);border-radius:8px;padding:1px 4px;font-size:3.6px;font-weight:900;margin-left:2px}
.rv-rate{position:absolute;right:8px;top:169px;font-size:5px;font-weight:900;display:flex;gap:2px;align-items:center}
.rv-rate i{font-style:normal;color:#9fadc6;font-weight:400}
.view-all{left:274px;top:1337px;width:90px;height:27px;border:1px solid #3b4d6c;border-radius:20px;display:flex;align-items:center;justify-content:center;gap:5px;font-size:6.4px;font-weight:900}

.light{position:absolute;left:0;top:0;width:638px;height:464px;background:var(--light);color:var(--ink)}
.light .sec-lede{color:#6c7a93}
.compare{top:205px;width:263px;height:108px;border-radius:0 0 8px 8px}
.compare-plain{left:50px;background:#e9edf4;border:1px solid #dde3ec;border-top:none}
.compare-best{left:325px;background:var(--navy);color:#fff;box-shadow:0 8px 20px rgba(14,24,41,.3)}
.compare ul{list-style:none;position:absolute;left:16px;top:14px;width:235px}
.compare li{display:flex;gap:6px;font-size:5.8px;line-height:8.5px;margin-bottom:9.5px}
.compare li svg{flex:none;margin-top:1px}
.keep{left:50px;top:335px;width:538px;height:87px;background:linear-gradient(90deg,#f6ede0,#faf3ea);border:1px solid #f0ddbf;border-radius:8px;text-align:center}
.keep h3{margin-top:16px;font-size:23px;color:var(--gold)}
.keep h3 small{font-family:"Lato",sans-serif;font-weight:700;font-size:6px;letter-spacing:-.2px}
.keep p{font-size:6px;line-height:11.5px;color:#5f6e88;margin-top:2px}

.step{top:640px;width:172px;height:138px;background:var(--card);border:1px solid var(--card-line);border-radius:8px}
.step-no{position:absolute;left:13px;top:15px;background:var(--gold);color:var(--ink);font-size:4.8px;font-weight:900;padding:3px 6px;border-radius:10px}
.step-ico{position:absolute;left:13px;top:38px;width:20px;height:20px;border:1px solid #4a5a78;border-radius:5px;display:flex;align-items:center;justify-content:center}
.step h4{position:absolute;left:13px;top:73px;font-size:7.4px;font-weight:900}
.step p{position:absolute;left:13px;top:89px;width:148px;font-size:5.6px;line-height:9px;color:#9fb0cc}
.pricing{left:50px;top:797px;width:538px;height:81px;background:var(--card);border:1px solid var(--card-line);border-radius:8px}
.pricing small{position:absolute;left:16px;top:15px;font-size:4.8px;font-weight:900;letter-spacing:.8px;color:var(--gold)}
.pricing h4{position:absolute;left:16px;top:27px;font-size:9.4px;font-weight:900}
.pricing p{position:absolute;left:16px;top:44px;width:260px;font-size:5.8px;line-height:9.5px;color:#9fb0cc}
.pricing .btn-gold{position:absolute;left:436px;top:26px;width:85px;height:27px;font-size:6.4px}
.quote{top:1000px;width:265px;height:108px;background:var(--card);border:1px solid var(--card-line);border-radius:8px}
.stars{position:absolute;left:14px;top:14px;display:flex;gap:2px}
.quote p{position:absolute;left:14px;top:30px;width:236px;font-size:5.9px;line-height:10px;font-style:italic;color:#c4cee0}
.who{position:absolute;left:14px;top:74px;display:flex;align-items:center;gap:6px}
.avatar{width:17px;height:17px;border-radius:50%;background:var(--gold);color:var(--ink);font-size:5px;font-weight:900;display:flex;align-items:center;justify-content:center}
.who b{display:block;font-size:6px}
.who span{display:block;font-size:4.8px;color:#9fb0cc;margin-top:2px}
.cta{left:50px;top:1153px;width:538px;height:192px;border-radius:8px;background:linear-gradient(135deg,#d08a2a 0%,#ecae50 30%,#e8a040 60%,#c77d1f 100%);color:var(--ink);text-align:center}
.cta h3{margin-top:32px;font-size:17.5px;line-height:31px}
.cta p{margin:10px auto 0;width:260px;font-size:6.6px;line-height:11px;color:#3b2a12}
.cta-btns{position:absolute;left:0;right:0;top:135px;display:flex;justify-content:center;gap:7px}
.cta-btns span{height:26px;border-radius:20px;display:flex;align-items:center;justify-content:center;font-size:6.6px;font-weight:900}
.cta-primary{width:115px;background:var(--navy);color:#fff}
.cta-ghost{width:73px;border:1px solid rgba(15,27,48,.45);color:var(--ink)}

.footer{position:absolute;left:0;top:1387px;width:638px;height:181px;background:#0b1424}
.footer .brand{left:50px;top:28px;font-size:10px}
.foot-about{left:50px;top:53px;width:122px;font-size:5.6px;line-height:9px;color:#9fb0cc}
.socials{left:50px;top:107px;display:flex;gap:6px}
.socials span{width:15px;height:15px;border-radius:50%;border:1px solid #2e3f5f}
.foot-col{top:29px}
.foot-col h5{font-size:5px;font-weight:900;letter-spacing:.8px;color:var(--gold);margin-bottom:12px}
.foot-col a{display:block;font-size:5.6px;color:#9fb0cc;margin-bottom:10.5px;text-decoration:none}
.news p{font-size:6.2px;line-height:10px;color:#d5dcea;width:130px;margin-bottom:6px}
.news-row{display:flex;gap:5px;align-items:center}
.news-input{width:95px;height:18px;border:1px solid #2e3f5f;border-radius:20px;font-size:5px;color:#6d7d99;display:flex;align-items:center;padding-left:8px}
.news .btn-gold{width:31px;height:18px;font-size:5.6px}
.foot-line{left:50px;top:149px;width:538px;height:1px;background:#1f2d47}
.foot-copy{left:50px;top:163px;font-size:4.8px;color:#6d7d99}
.foot-legal{right:50px;top:163px;display:flex;gap:10px;font-size:4.8px;color:#6d7d99}
</style>
</head>
<body>

<section class="page page-home">
  <div class="hero" role="img" aria-label="Camper van parked at dusk beside a campfire with mountains and pine trees behind"></div>

  <header class="nav">
    <div class="brand">Zandoprik</div>
    <nav class="nav-links"><span>RV Rentals</span><span>How It Works</span><span>For Owners</span><span>FAQ</span></nav>
    <span class="nav-signin">Sign in</span>
    <span class="nav-cta btn-gold">List your RV</span>
  </header>

  <div class="abs hero-badge">✓ LIST IT · RENT IT · BANK IT</div>
  <h1 class="abs head hero-title">Find the best RV rentals <span>in the country.</span></h1>
  <p class="abs hero-lede">Explore the open road in the perfect RV rental — or get one delivered and set up for you. <b>One flat monthly rate.</b> No commissions. No hidden fees. Renters save, owners earn more.</p>

  <div class="abs search">
    <div class="search-tabs">
      <span class="on">⛟ Pick up &amp; hit the road</span>
      <span class="off">◈ Get it delivered</span>
    </div>
    <div class="search-line"></div>
    <div class="field" style="left:6px;width:113px"><label>LOCATION</label>
      <div class="box"><svg width="7" height="7" viewBox="0 0 24 24" fill="none" stroke="#e49a2f" stroke-width="2.5"><path d="M12 22s7-7 7-12a7 7 0 0 0-14 0c0 5 7 12 7 12z"/><circle cx="12" cy="10" r="2.5"/></svg>Where to?</div></div>
    <div class="field" style="left:124px;width:80px"><label>DATES</label>
      <div class="box"><svg width="7" height="7" viewBox="0 0 24 24" fill="none" stroke="#e49a2f" stroke-width="2.5"><rect x="3" y="5" width="18" height="16" rx="2"/><path d="M3 10h18M8 3v4M16 3v4"/></svg>Any dates</div></div>
    <div class="field" style="left:209px;width:80px"><label>GUESTS</label>
      <div class="box"><svg width="7" height="7" viewBox="0 0 24 24" fill="none" stroke="#e49a2f" stroke-width="2.5"><circle cx="9" cy="8" r="3.5"/><path d="M2 20c0-4 3-6 7-6s7 2 7 6M16 5a3 3 0 0 1 0 6M22 20c0-3-2-5-4-5.5"/></svg>2 guests</div></div>
    <div class="field" style="left:293px;width:80px"><label>DRIVER'S AGE</label>
      <div class="box"><svg width="7" height="7" viewBox="0 0 24 24" fill="none" stroke="#e49a2f" stroke-width="2.5"><circle cx="12" cy="12" r="9"/><path d="M12 7v5l3 2"/></svg>25+</div></div>
    <div class="search-btn btn-gold">Search <svg width="6" height="6" viewBox="0 0 24 24" fill="none" stroke="#0f1b30" stroke-width="3"><circle cx="10" cy="10" r="7"/><path d="M15 15l6 6"/></svg></div>
  </div>

  <div class="abs popular">Popular:
    <span class="chip">Camper van</span><span class="chip">Pets welcome</span><span class="chip">Value</span><span class="chip">Vintage</span><span class="chip">Small trailer</span>
  </div>

  <div class="abs hero-divider"></div>
  <div class="abs stat" style="left:39px"><b>$0</b><span>commission on every rental</span></div>
  <div class="abs stat-sep" style="left:132px"></div>
  <div class="abs stat" style="left:142px"><b>100%</b><span>of earnings stay with owners</span></div>
  <div class="abs stat-sep" style="left:236px"></div>
  <div class="abs stat" style="left:246px"><b>1</b><span>flat monthly rate — that's it</span></div>
  <div class="abs stat-sep" style="left:340px"></div>
  <div class="abs stat" style="left:350px"><b>$1M</b><span>liability protection included</span></div>

  <div class="abs mode" style="left:50px">
    <div class="mode-photo" role="img" aria-label="Trailer with string lights set up at a forest campsite at night" style="background:linear-gradient(90deg,rgba(14,24,41,.85),rgba(14,24,41,.2)),linear-gradient(170deg,#24406a 0%,#2b3c58 40%,#7a5431 75%,#2a2418 100%)"></div>
    <div class="mode-copy"><h3 class="head">Get it delivered</h3><p>Less set up. More quality time. Love camping but don't love driving? Get an RV delivered and set up at a location of your choice.</p></div>
    <span class="mode-btn btn-gold">Get it delivered</span>
  </div>
  <div class="abs mode" style="left:325px">
    <div class="mode-photo" role="img" aria-label="Motorhome driving a winding mountain road at sunset" style="background:linear-gradient(90deg,rgba(14,24,41,.85),rgba(14,24,41,.15)),linear-gradient(175deg,#2c3d5c 0%,#c0783a 30%,#4c4f5c 55%,#3a4048 100%)"></div>
    <div class="mode-copy"><h3 class="head">Pick it up &amp; hit the road</h3><p>Get ready for the ultimate road trip. Pick up an RV near you, or at a destination of your choice — and keep more of your budget for the journey.</p></div>
    <span class="mode-btn btn-gold">Pick it up</span>
  </div>

  <div class="rule" style="top:756px"></div>
  <div class="eyebrow" style="top:767px">Featured on Zandoprik</div>
  <h2 class="sec-title head" style="top:792px">Find the best RV rentals in the<br>country</h2>
  <p class="sec-lede" style="top:844px;width:330px">Explore the open road in the perfect RV rental. Every listing is from a verified owner — with no commission, you'll find more value per night.</p>

  <div class="abs filters">
    <span class="chip on">Popular</span><span class="chip">Camper van</span><span class="chip">Travel trailer</span><span class="chip">Class C</span><span class="chip">Vintage</span><span class="chip">Class A</span>
  </div>

  <article class="abs rv" style="left:50px;top:922px">
    <div class="rv-photo" role="img" aria-label="Camper van on a coastal cliff at sunset" style="background:linear-gradient(180deg,#3c5578,#c48047 45%,#33435a 75%,#1d2838)"></div>
    <span class="rv-tag">Top rated</span>
    <span class="rv-fav"><svg width="7" height="7" viewBox="0 0 24 24" fill="none" stroke="#fff" stroke-width="2.5"><path d="M12 21s-8-5-8-11a4.5 4.5 0 0 1 8-3 4.5 4.5 0 0 1 8 3c0 6-8 11-8 11z"/></svg></span>
    <div class="rv-meta">Camper van · Sleeps 2 · 17 ft</div>
    <div class="rv-name">Blue Ridge Voyager</div>
    <div class="rv-loc">⌖ Asheville, NC</div>
    <div class="rv-line"></div>
    <div class="rv-price"><b>$119</b>/night<span class="fee">0% FEE</span></div>
    <div class="rv-rate"><span style="color:#e49a2f">★</span>5.0 <i>(41)</i></div>
  </article>
  <article class="abs rv" style="left:233px;top:922px">
    <div class="rv-photo" role="img" aria-label="Travel trailer with string lights and a campfire in a forest" style="background:linear-gradient(180deg,#3a4d68,#4d5a66 45%,#8a6138 75%,#2a2a26)"></div>
    <span class="rv-tag">Instant book</span>
    <span class="rv-fav"><svg width="7" height="7" viewBox="0 0 24 24" fill="none" stroke="#fff" stroke-width="2.5"><path d="M12 21s-8-5-8-11a4.5 4.5 0 0 1 8-3 4.5 4.5 0 0 1 8 3c0 6-8 11-8 11z"/></svg></span>
    <div class="rv-meta">Travel trailer · Sleeps 6 · 26 ft</div>
    <div class="rv-name">Pinecrest Lite 26</div>
    <div class="rv-loc">⌖ Denver, CO</div>
    <div class="rv-line"></div>
    <div class="rv-price"><b>$139</b>/night<span class="fee">0% FEE</span></div>
    <div class="rv-rate"><span style="color:#e49a2f">★</span>4.9 <i>(28)</i></div>
  </article>
  <article class="abs rv" style="left:416px;top:922px">
    <div class="rv-photo" role="img" aria-label="Class C motorhome in a wildflower meadow below mountains" style="background:linear-gradient(180deg,#4a5a86,#7c8aa8 35%,#4f6a4c 65%,#6a5a7a)"></div>
    <span class="rv-tag">Family favorite</span>
    <span class="rv-fav"><svg width="7" height="7" viewBox="0 0 24 24" fill="none" stroke="#fff" stroke-width="2.5"><path d="M12 21s-8-5-8-11a4.5 4.5 0 0 1 8-3 4.5 4.5 0 0 1 8 3c0 6-8 11-8 11z"/></svg></span>
    <div class="rv-meta">Class C · Sleeps 7 · 28 ft</div>
    <div class="rv-name">Ridge Rover C-28</div>
    <div class="rv-loc">⌖ Phoenix, AZ</div>
    <div class="rv-line"></div>
    <div class="rv-price"><b>$179</b>/night<span class="fee">0% FEE</span></div>
    <div class="rv-rate"><span style="color:#e49a2f">★</span>4.8 <i>(33)</i></div>
  </article>

  <article class="abs rv" style="left:50px;top:1125px">
    <div class="rv-photo" role="img" aria-label="Vintage aluminium trailer in the desert at dusk" style="background:linear-gradient(180deg,#3a4668,#b86f45 40%,#5a4a48 70%,#2a2a32)"></div>
    <span class="rv-tag">Pet friendly</span>
    <span class="rv-fav"><svg width="7" height="7" viewBox="0 0 24 24" fill="none" stroke="#fff" stroke-width="2.5"><path d="M12 21s-8-5-8-11a4.5 4.5 0 0 1 8-3 4.5 4.5 0 0 1 8 3c0 6-8 11-8 11z"/></svg></span>
    <div class="rv-meta">Vintage trailer · Sleeps 4 · 24 ft</div>
    <div class="rv-name">Silver Dune Classic</div>
    <div class="rv-loc">⌖ Tucson, AZ</div>
    <div class="rv-line"></div>
    <div class="rv-price"><b>$149</b>/night<span class="fee">0% FEE</span></div>
    <div class="rv-rate"><span style="color:#e49a2f">★</span>5.0 <i>(52)</i></div>
  </article>
  <article class="abs rv" style="left:233px;top:1125px">
    <div class="rv-photo" role="img" aria-label="Class A motorhome by a mountain lake at night" style="background:linear-gradient(180deg,#2d3d5e,#5a6a86 35%,#7a5530 65%,#1e2636)"></div>
    <span class="rv-tag">Luxury</span>
    <span class="rv-fav"><svg width="7" height="7" viewBox="0 0 24 24" fill="none" stroke="#fff" stroke-width="2.5"><path d="M12 21s-8-5-8-11a4.5 4.5 0 0 1 8-3 4.5 4.5 0 0 1 8 3c0 6-8 11-8 11z"/></svg></span>
    <div class="rv-meta">Class A · Sleeps 8 · 35 ft</div>
    <div class="rv-name">Summit Cruiser A-35</div>
    <div class="rv-loc">⌖ Seattle, WA</div>
    <div class="rv-line"></div>
    <div class="rv-price"><b>$249</b>/night<span class="fee">0% FEE</span></div>
    <div class="rv-rate"><span style="color:#e49a2f">★</span>4.9 <i>(19)</i></div>
  </article>
  <article class="abs rv" style="left:416px;top:1125px">
    <div class="rv-photo" role="img" aria-label="Toy hauler trailer lit up among red rock canyons" style="background:linear-gradient(180deg,#34426a,#8a5a4a 40%,#9a5a34 65%,#2e2422)"></div>
    <span class="rv-tag">Adventure</span>
    <span class="rv-fav"><svg width="7" height="7" viewBox="0 0 24 24" fill="none" stroke="#fff" stroke-width="2.5"><path d="M12 21s-8-5-8-11a4.5 4.5 0 0 1 8-3 4.5 4.5 0 0 1 8 3c0 6-8 11-8 11z"/></svg></span>
    <div class="rv-meta">Toy hauler · Sleeps 6 · 30 ft</div>
    <div class="rv-name">Canyon Hauler 27</div>
    <div class="rv-loc">⌖ Moab, UT</div>
    <div class="rv-line"></div>
    <div class="rv-price"><b>$199</b>/night<span class="fee">0% FEE</span></div>
    <div class="rv-rate"><span style="color:#e49a2f">★</span>4.9 <i>(24)</i></div>
  </article>

  <div class="abs view-all">View all RVs <svg width="6" height="6" viewBox="0 0 24 24" fill="none" stroke="#fff" stroke-width="3"><path d="M4 12h16M14 6l6 6-6 6"/></svg></div>
</section>

<section class="page page-owners">
  <div class="light">
    <div class="rule" style="top:42px"></div>
    <div class="eyebrow" style="top:54px">Why Zandoprik</div>
    <h2 class="sec-title head" style="top:78px;color:var(--ink)">The only RV marketplace that<br>never takes a cut</h2>
    <p class="sec-lede" style="top:130px;width:330px">Other sites charge 20% or more of every single rental. Zandoprik charges one flat monthly rate — so owners keep 100% of their earnings, and renters get better value.</p>

    <div class="abs compare compare-plain">
      <ul>
        <li><svg width="6" height="6" viewBox="0 0 24 24" stroke="#d9463b" stroke-width="3"><path d="M5 5l14 14M19 5L5 19"/></svg><span>Take <b>20% or more</b> in commission from every rental</span></li>
        <li><svg width="6" height="6" viewBox="0 0 24 24" stroke="#d9463b" stroke-width="3"><path d="M5 5l14 14M19 5L5 19"/></svg><span>Service fees, booking fees &amp; add-on charges shrink your payout</span></li>
        <li><svg width="6" height="6" viewBox="0 0 24 24" stroke="#d9463b" stroke-width="3"><path d="M5 5l14 14M19 5L5 19"/></svg><span>Owners price higher just to cover fees — fewer bookings, less profit</span></li>
        <li><svg width="6" height="6" viewBox="0 0 24 24" stroke="#d9463b" stroke-width="3"><path d="M5 5l14 14M19 5L5 19"/></svg><span>Your income drops with every single booking</span></li>
      </ul>
    </div>
    <div class="abs compare compare-best">
      <ul>
        <li><svg width="7" height="7" viewBox="0 0 24 24" fill="none" stroke="#e49a2f" stroke-width="2.5"><circle cx="12" cy="12" r="9"/><path d="M8 12l3 3 5-6"/></svg><span><b>Zero commission.</b> One flat monthly rate, that's it</span></li>
        <li><svg width="7" height="7" viewBox="0 0 24 24" fill="none" stroke="#e49a2f" stroke-width="2.5"><circle cx="12" cy="12" r="9"/><path d="M8 12l3 3 5-6"/></svg><span><b>Keep 100%</b> of every rental — we never touch your earnings</span></li>
        <li><svg width="7" height="7" viewBox="0 0 24 24" fill="none" stroke="#e49a2f" stroke-width="2.5"><circle cx="12" cy="12" r="9"/><path d="M8 12l3 3 5-6"/></svg><span>Payments, insurance &amp; 24/7 roadside assistance included</span></li>
        <li><svg width="7" height="7" viewBox="0 0 24 24" fill="none" stroke="#e49a2f" stroke-width="2.5"><circle cx="12" cy="12" r="9"/><path d="M8 12l3 3 5-6"/></svg><span>No hidden fees for renters either — transparent pricing, always</span></li>
      </ul>
    </div>

    <div class="abs keep">
      <h3 class="head">Keep 100%<small>of your earnings</small></h3>
      <p>On a $2,000 weekly rental, other platforms keep up to $400+ in commission.<br>With Zandoprik, the full $2,000 is yours — every single time.</p>
    </div>
  </div>

  <div class="rule" style="top:505px"></div>
  <div class="eyebrow" style="top:517px">For owners</div>
  <h2 class="sec-title head" style="top:541px">Turn your RV into income in 3<br>steps</h2>
  <p class="sec-lede" style="top:594px;width:300px">List in minutes, get booked, and keep everything you earn. No commission. No complicated fee structures. Just one flat monthly rate.</p>

  <div class="abs step" style="left:50px">
    <span class="step-no">STEP 01</span>
    <span class="step-ico"><svg width="9" height="9" viewBox="0 0 24 24" fill="none" stroke="#e49a2f" stroke-width="2"><rect x="3" y="5" width="18" height="12" rx="2"/><path d="M7 17v3M17 17v3M3 11h18"/></svg></span>
    <h4>List your RV in minutes</h4>
    <p>Add photos, set your nightly price and availability. Free to list — you only pay one flat monthly rate when you're active.</p>
  </div>
  <div class="abs step" style="left:233px">
    <span class="step-no">STEP 02</span>
    <span class="step-ico"><svg width="9" height="9" viewBox="0 0 24 24" fill="none" stroke="#e49a2f" stroke-width="2"><circle cx="12" cy="12" r="9"/><path d="M8 12l3 3 5-6"/></svg></span>
    <h4>Get booked, worry-free</h4>
    <p>We handle secure payments, renter screening and $1M liability protection. 24/7 roadside assistance rides along on every trip.</p>
  </div>
  <div class="abs step" style="left:416px">
    <span class="step-no">STEP 03</span>
    <span class="step-ico"><svg width="9" height="9" viewBox="0 0 24 24" fill="none" stroke="#e49a2f" stroke-width="2"><circle cx="12" cy="12" r="9"/><path d="M15 9h-4a2 2 0 0 0 0 4h2a2 2 0 0 1 0 4H9M12 6v2M12 17v2"/></svg></span>
    <h4>Keep 100% of earnings</h4>
    <p>Every dollar from every rental lands in your account. Your monthly rate covers everything — no surprises, no deductions.</p>
  </div>

  <div class="abs pricing">
    <small>SIMPLE PRICING</small>
    <h4>One flat monthly rate. Zero commission. Ever.</h4>
    <p>No percentage cuts. No per-booking fees. No tiered commissions that eat your profit as you grow. The math is simple: the more you rent, the more you keep.</p>
    <span class="btn-gold">Become a host</span>
  </div>

  <div class="rule" style="top:920px"></div>
  <div class="eyebrow" style="top:931px">Loved by hosts &amp; renters</div>
  <h2 class="sec-title head" style="top:956px">Renters save. Owners earn.</h2>

  <div class="abs quote" style="left:50px">
    <div class="stars"><span style="color:#e49a2f;font-size:7px;letter-spacing:1px">★★★★★</span></div>
    <p>"I rented my Class C out 9 weekends last summer. On other platforms I'd have given up almost $1,400 in commission. With Zandoprik that money stayed in my pocket. I'll never list anywhere else."</p>
    <div class="who"><span class="avatar">DK</span><div><b>Dario K.</b><span>Host · Montana</span></div></div>
  </div>
  <div class="abs quote" style="left:324px">
    <div class="stars"><span style="color:#e49a2f;font-size:7px;letter-spacing:1px">★★★★★</span></div>
    <p>"No service fee on top of every night made the exact same camper van $180 cheaper for our 2-week trip. The rental itself was flawless — clean rig, great owner, easy pickup."</p>
    <div class="who"><span class="avatar">LP</span><div><b>Lena P.</b><span>Renter · Austin, TX</span></div></div>
  </div>

  <div class="abs cta">
    <h3 class="head">Own an RV? Turn it into<br>income.</h3>
    <p>Join the marketplace where owners keep 100% of every rental. One flat monthly rate. No commission. No hidden fees.</p>
    <div class="cta-btns"><span class="cta-primary">List your RV — it's free</span><span class="cta-ghost">Rent an RV</span></div>
  </div>

  <footer class="footer">
    <div class="brand">Zandoprik</div>
    <p class="abs foot-about">The peer-to-peer RV rental marketplace where owners keep 100% of every rental. One flat monthly rate. No commissions, ever.</p>
    <div class="abs socials"><span></span><span></span><span></span><span></span></div>
    <div class="abs foot-col" style="left:185px"><h5>RENT AN RV</h5><a>Camper vans</a><a>Travel trailers</a><a>Class A &amp; C</a><a>Vintage &amp; retro</a><a>Delivered to you</a></div>
    <div class="abs foot-col" style="left:275px"><h5>OWNERS</h5><a>How it works</a><a>Pricing &amp; fees</a><a>Protection &amp; insurance</a><a>Become a host</a><a>Host success stories</a></div>
    <div class="abs foot-col" style="left:366px"><h5>COMPANY</h5><a>About us</a><a>Campgrounds</a><a>Support</a><a>Safety &amp; trust</a><a>Careers</a></div>
    <div class="abs foot-col news" style="left:457px"><h5>STAY IN THE LOOP</h5><p>Get new listings, road-trip guides and host tips in your inbox.</p>
      <div class="news-row"><span class="news-input">Your email</span><span class="btn-gold">Join</span></div></div>
    <div class="abs foot-line"></div>
    <div class="abs foot-copy">© 2026 Zandoprik. All rights reserved.</div>
    <div class="abs foot-legal"><span>Privacy</span><span>Terms</span><span>Cookies</span></div>
  </footer>
</section>

</body>
</html>
```